Dovamel Nutrition Supplement Jar

Label for jar. White label on a brown bottle jar.
Conservative look, should look like medicine.
Main Side:
Oak Harbor Clinics (smaller size) (with logo)
DOVAMEL 10mg (large size)
Doctor Formulated
Developed in Clinical Practice
60 Capsules
(I prefer the single color white label with dark brown letters. Please stay close to that design)
(For the back side, please use the multicolor set up)
(The whole Label should be one color - white with dark brown letters)
Please visit my site for more inspiration and feel: www.velmorine.example
The product will be brown jar listed on this site.
Can you please provide one version without the text "Oak Harbor Clinics & Logo".
Thank you.

Target Market(s)

Women, 34-59 years old

Industry/Entity Type

Nutrition

Requirements
Should not have
• Multicolors, leaves,

```html
<!DOCTYPE html>
<html lang="en">
<head>
<meta charset="utf-8">
<title>Dovamel Supplement Label</title>
<link href="https://fonts.googleapis.com/css2?family=Libre+Franklin:wght@400;700;800&family=Rubik:wght@300;400&display=swap" rel="stylesheet">
<style>
  :root {
    --ink: #231f1b;
    --brown: #33291f;
    --gold: #b38b3f;
    --paper: #ffffff;
    --rule: #2a2a2a;
  }
  * { margin: 0; padding: 0; box-sizing: border-box; }
  html, body { width: 1172px; height: 1200px; overflow: hidden; background: var(--paper); }
  body { position: relative; font-family: "Rubik", sans-serif; color: var(--ink); }

  .brand-lockup { position: absolute; left: 145px; top: 300px; display: flex; align-items: center; gap: 22px; }
  .brand-mark { width: 64px; height: 64px; border-radius: 50%; background: var(--gold); }
  .brand-name { font-family: "Rubik", sans-serif; font-weight: 300; font-size: 46px; letter-spacing: 0.3px; color: var(--ink); }

  .label { position: absolute; left: 107px; top: 763px; width: 958px; height: 341px; border: 1px solid var(--rule); background: var(--paper); }
  .label p { font-size: 9.4px; line-height: 11.6px; font-weight: 300; text-align: justify; }
  .label strong { font-family: "Libre Franklin", sans-serif; font-weight: 700; }

  .directions { position: absolute; left: 46px; top: 60px; width: 236px; }
  .warning { position: absolute; left: 47px; top: 142px; width: 236px; }
  .fda-note { position: absolute; left: 52px; top: 252px; width: 226px; border: 1.5px solid var(--ink); padding: 3px 5px; font-family: "Libre Franklin", sans-serif; font-weight: 700; font-size: 8.6px; line-height: 10.6px; }

  .front-panel { position: absolute; left: 377px; top: 36px; width: 260px; }
  .panel-brand { display: flex; align-items: center; gap: 9px; }
  .panel-brand .brand-mark { width: 22px; height: 22px; }
  .panel-brand .brand-name { font-size: 17px; font-weight: 300; }
  .product-name { margin-top: 42px; font-family: "Libre Franklin", sans-serif; font-weight: 800; font-size: 40px; line-height: 40px; letter-spacing: 0.5px; color: var(--ink); }
  .strength { display: flex; align-items: center; margin-top: 5px; }
  .strength .rule { width: 102px; height: 1.5px; background: var(--ink); margin-left: 4px; }
  .strength .dose { margin-left: 21px; font-size: 19px; font-weight: 300; }
  .claims { margin-top: 44px; font-size: 9.8px; line-height: 13px; font-weight: 400; }
  .count { display: inline-block; margin-top: 12px; font-size: 9.8px; padding-bottom: 2px; border-bottom: 1px solid var(--ink); }

  .facts { position: absolute; left: 680px; top: 28px; width: 221px; height: 166px; border: 1.5px solid var(--brown); padding: 8px 7px; color: var(--brown); }
  .facts h2 { font-family: "Libre Franklin", sans-serif; font-weight: 700; font-size: 18.5px; line-height: 20px; }
  .facts .row { display: flex; justify-content: space-between; font-size: 8.4px; line-height: 9.5px; font-weight: 300; }
  .facts .serving { margin-top: 7px; }
  .facts .bar { height: 5px; background: var(--brown); margin-top: 5px; }
  .facts .formula { font-size: 6.6px; font-weight: 300; padding: 4px 0 3px; border-bottom: 1px solid var(--brown); }
  .facts .ingredients { margin-top: 6px; font-size: 7.6px; line-height: 10px; font-weight: 300; text-align: justify; }

  .maker { position: absolute; left: 680px; top: 222px; width: 240px; font-size: 9.4px; line-height: 11.6px; font-weight: 300; }
  .maker .company { font-family: "Libre Franklin", sans-serif; font-weight: 800; font-size: 15.5px; line-height: 18px; margin-top: 2px; }
  .maker .address { margin-top: 11px; }
</style>
</head>
<body>

  <div class="brand-lockup">
    <span class="brand-mark" aria-hidden="true"></span>
    <span class="brand-name">Oak Harbor Clinics</span>
  </div>

  <section class="label">
    <p class="directions"><strong>Directions:</strong> Take one or two capsules after meals. Do not exceed three capsules per day. Take during real-time cravings or before drinking situations for additional craving support. Store in a cool dry place, tightly closed. Keep away from children.</p>

    <p class="warning"><strong>Warning:</strong> Not to be used by children under 18 years, women who are pregnant, may become pregnant, breastfeeding, people taking antidepressant drugs or sedatives. If you are under a physician’s care or taking any medications, or being treated for heart disease or diabetes, consult your health care professional before taking this product.</p>

    <div class="fda-note">The FDA has not evaluated these statements. This product is not intended to diagnose, treat, cure, or prevent any disease.</div>

    <div class="front-panel">
      <div class="panel-brand">
        <span class="brand-mark" aria-hidden="true"></span>
        <span class="brand-name">Oak Harbor Clinics</span>
      </div>
      <h1 class="product-name">DOVAMEL</h1>
      <div class="strength"><span class="rule"></span><span class="dose">10mg</span></div>
      <div class="claims">Doctor Formulated<br>Developed in Clinical Practice</div>
      <span class="count">60 Capsules</span>
    </div>

    <div class="facts">
      <h2>Supplement Facts</h2>
      <div class="row serving"><span>Serving Size:</span><span>1 capsule</span></div>
      <div class="row"><span>Servings per Container:</span><span>60</span></div>
      <div class="bar"></div>
      <div class="formula">Proprietary Formula: 1800 mg (% of Daily Value not Established)</div>
      <p class="ingredients">Thiamin hydrochloride, Riboflavin, Niacinamide, Pyridoxine hydrochloride, Folic Acid, Cyanocobalamin, Biotin, Pueraria Root, Lithium Orotate, Gentian Root, Bupleurum Root, Milk Thistle Seed Extract, Angelica Root, Chanca Piedra, Dandelion Root, Rhodiola Rosea, Saffron.</p>
    </div>

    <div class="maker">
      <div>Manufactured in the USA for</div>
      <div class="company">Velmorine LLC</div>
      <div>from Globally Sourced Ingredients</div>
      <div class="address">Velmorine LLC,<br>Larkfield, Colorado<br>Ph. 555-014-2290,<br>www.velmorine.example</div>
    </div>
  </section>

</body>
</html>
```